Metal fabrication company website refresh

Our client want's a fresh look to their website
https://www.kolvendaworks.com.au/

They may use a video as their hero shot, but like product photos.

Current logo is here: https://www.kolvendaworks.com.au/wp-content/uploads/2015/05/logo.png
Current logo with slogan is here: https://www.kolvendaworks.com.au/wp-content/uploads/2023/10/kolvenda_logo_with_slogan.jpg

Colors should be masculine, but they want a little more 'personal' feeling. We may be able to achieve this with photos of the staff or maybe a drone video. They like photos and sliders.

They use their certifications on their emails, and the ISO certifications are the most important so if you can find a nice way to show them but not so they stand out too much it would be nice. Their certification logos that they use in their email are here: https://www.kolvendaworks.com.au/wp-content/uploads/2023/10/kolvenda_certifications.pdf

They would prefer to go to a more 'one page' approach with some secondary pages like projects, about, products linked from a home page summary

```html
<!DOCTYPE html>
<html lang="en">
<head>
<meta charset="utf-8">
<title>Kolvenda Works — Quality &amp; Craftsmanship</title>
<link href="https://fonts.googleapis.com/css2?family=Outfit:wght@400;500;600;700&display=swap" rel="stylesheet">
<style>
:root{
  --green:#4fa61a;
  --green-bright:#56b51c;
  --ink:#121212;
  --ink-2:#0b0b0b;
  --white:#ffffff;
  --muted:#d6d6d6;
}
*{box-sizing:border-box;margin:0;padding:0}
html,body{width:1200px;height:4594px;overflow:hidden}
body{background:var(--ink);color:var(--white);font-family:"Outfit",sans-serif;position:relative}
.abs{position:absolute}
.btn{position:absolute;background:var(--green);color:var(--white);font-size:13px;font-weight:500;display:flex;align-items:center;justify-content:center;text-decoration:none}
.photo{position:absolute}

/* hero */
.hero{position:absolute;left:0;top:0;width:1200px;height:562px}
.hero .shade{position:absolute;inset:0;background:rgba(0,0,0,.35)}
.brand{position:absolute;display:flex;align-items:center;gap:10px;color:var(--white);font-weight:500;white-space:nowrap}
.brand i{display:block;background:var(--green)}
.nav{position:absolute;display:flex;gap:40px;font-size:13px}
.nav a{color:var(--white);text-decoration:none}
.hero h1{position:absolute;left:0;width:1200px;top:196px;text-align:center;font-size:54px;line-height:54px;font-weight:600}
.hero .lede{position:absolute;left:0;width:1200px;top:329px;text-align:center;font-size:14px}

/* about */
.about .eyebrow{font-size:12px;display:flex;align-items:center;gap:10px}
.about .eyebrow span{display:inline-block;width:20px;height:2px;background:var(--green)}
.about h2{font-size:38px;font-weight:600;white-space:nowrap}
.about .sub{color:var(--green-bright);font-size:15px}
.about p{font-size:12.5px;line-height:23px;width:436px}
.stat{position:absolute;top:1086px;height:125px;padding:22px 22px}
.stat b{display:block;font-size:32px;font-weight:600;line-height:34px}
.stat small{display:block;font-size:13px;line-height:19px;margin-top:8px}

/* products */
.products{position:absolute;left:0;top:1302px;width:1200px;height:1114px;background:linear-gradient(180deg,#2b3136 0%,#23282a 45%,#26301e 100%)}
.section-title{position:absolute;left:0;width:1200px;text-align:center;font-size:36px;font-weight:600}
.card{position:absolute;width:278px;height:376px;border:1px solid #bdbdbd}
.card span{position:absolute;left:0;right:0;bottom:16px;text-align:center;font-size:16px}

/* feature */
.feature h3{font-size:26px;font-weight:500;line-height:36px}
.feature p{font-size:12px;line-height:22px;width:440px}

/* gallery */
.gallery{position:absolute;left:0;top:3120px;width:1200px;height:746px;background:linear-gradient(160deg,#2a2f33 0%,#1f2326 60%,#2b2f2a 100%)}
.tile{position:absolute}

/* safety */
.safety{position:absolute;left:0;top:3940px;width:1200px;text-align:center;font-size:30px;font-weight:500;line-height:39px}

/* footer */
.footer{position:absolute;left:0;top:4217px;width:1200px;height:326px;background:#141414}
.rule{position:absolute;left:160px;top:4427px;width:880px;height:1px;background:#333}
.contact{position:absolute;top:4462px;display:flex;align-items:center;gap:12px;font-size:12px;line-height:19px}
.contact .ico{width:38px;height:38px;border:1.5px solid var(--green);border-radius:50%;display:flex;align-items:center;justify-content:center}
.bar{position:absolute;left:0;top:4543px;width:1200px;height:51px;background:var(--green);font-size:12px}
.bar .l{position:absolute;left:164px;top:18px}
.bar .r{position:absolute;right:162px;top:18px}
</style>
</head>
<body>

<!-- Hero -->
<section class="hero">
  <div class="photo" role="img" aria-label="Stainless steel handrail on a stone staircase" style="inset:0;background:linear-gradient(115deg,#202020 0%,#3d3a36 40%,#6e5b4a 68%,#3a2a1f 100%)"></div>
  <div class="shade"></div>
  <div class="brand" style="left:160px;top:24px;font-size:28px"><i style="width:14px;height:14px"></i>Kolvenda Works</div>
  <nav class="nav" style="left:575px;top:33px"><a>Home</a><a>Projects</a><a>About</a><a>Products</a></nav>
  <a class="btn" style="left:918px;top:21px;width:120px;height:41px">Contact Us</a>
  <h1>Quality &amp;<br>Craftsmanship</h1>
  <div class="lede">Accredited standards, elegant and affordable</div>
  <a class="btn" style="left:517px;top:376px;width:166px;height:41px">View Our Products</a>
</section>

<!-- About -->
<section class="about">
  <div class="photo" role="img" aria-label="Curved steel handrails along concrete steps" style="left:160px;top:645px;width:377px;height:525px;background:linear-gradient(180deg,#5d6a45 0%,#8f8d7e 45%,#a29f95 100%)"></div>
  <div class="abs eyebrow" style="left:605px;top:650px">Who We Are <span></span></div>
  <h2 class="abs" style="left:604px;top:668px">About Kolvenda Works</h2>
  <div class="abs sub" style="left:605px;top:723px">Boundary Supply Is Now Kolvenda. Pty Ltd.</div>
  <p class="abs" style="left:604px;top:752px">We chose to re-brand as our growth in custom fabrication and projects has grown beyond our traditional perimeter fencing products. We make custom products and can now deliver a truly comprehensive range of metal products for just about any project.</p>
  <p class="abs" style="left:604px;top:849px">boundarysupply.com.au emails and web address will continue to operate, but our new website and email addresses have become kolvendaworks.com.au.</p>
  <a class="btn" style="left:604px;top:931px;width:136px;height:41px">Read More</a>
  <div class="stat" style="left:428px;width:203px;background:var(--green)"><b>38</b><small>Lorem Ipsu Dolor Sit Amet Ctetur</small></div>
  <div class="stat" style="left:631px;width:203px;background:var(--ink-2)"><b>2000</b><small>Lorem Ipsu Dolor Sit Amet Ctetur</small></div>
  <div class="stat" style="left:834px;width:206px;background:var(--green)"><b>$10B+</b><small>Sit Amet Ctetur Rem Ipsu Dolor</small></div>
</section>

<!-- Products -->
<section class="products" role="img" aria-label="Chainwire fence on a grass field at dusk"></section>
<div class="abs" style="left:0;top:1302px;width:1200px;height:1114px;background:rgba(0,0,0,.35)"></div>
<h2 class="section-title" style="top:1380px">Our Products</h2>
<div class="abs" style="left:0;width:1200px;top:1440px;text-align:center;font-size:15px">Browse Our Extensive Range of Products And Custom Fabrication.</div>
<div class="card" role="img" aria-label="Aluminium screens on a building" style="left:160px;top:1487px;background:linear-gradient(180deg,#8fb0d6 0%,#a9abae 45%,#585c60 100%)"><span>Aluminium Screens</span></div>
<div class="card" role="img" aria-label="Chainwire fencing around a field" style="left:460px;top:1487px;background:linear-gradient(180deg,#a7c3e0 0%,#7c8a68 55%,#5d7a3c 100%)"><span>Chainwire Fencing</span></div>
<div class="card" role="img" aria-label="Automated boom gate" style="left:761px;top:1487px;background:linear-gradient(180deg,#9fbfe2 0%,#7d8a75 55%,#6b6a66 100%)"><span>Gate Automation</span></div>
<div class="card" role="img" aria-label="Timber steps with steel handrails by water" style="left:160px;top:1879px;background:linear-gradient(180deg,#8d9598 0%,#6e6a5a 50%,#7a5535 100%)"><span>Handrails</span></div>
<div class="card" role="img" aria-label="High security fence with razor wire" style="left:460px;top:1879px;background:linear-gradient(180deg,#6f9fd8 0%,#5d6670 50%,#3c3f44 100%)"><span>High Security Fencing</span></div>
<div class="card" role="img" aria-label="Black tubular steel gate" style="left:761px;top:1879px;background:linear-gradient(180deg,#5d8fd6 0%,#6c8248 50%,#3a3a36 100%)"><span>Tubular Fencing</span></div>
<a class="btn" style="left:519px;top:2286px;width:166px;height:41px">View All Products</a>

<!-- Feature -->
<section class="feature">
  <h3 class="abs" style="left:164px;top:2660px">Duis Faucibus Tincidunt Veitid Dimt<br>Dapib Ex Tempor</h3>
  <p class="abs" style="left:162px;top:2740px">Lorem ipsum dolor sit amet, consectetuer adipiscing elit, sed diam nonummy nibh euismod tincidunt ut laoreet dolore magna aliquam erat volutpat. Ut wisi enim ad minim veniam.</p>
  <a class="btn" style="left:160px;top:2828px;width:122px;height:41px">Contact Us</a>
  <div class="photo" role="img" aria-label="Chainwire fence and guard rail beside a concrete road" style="left:663px;top:2507px;width:377px;height:524px;background:linear-gradient(180deg,#a9aeb3 0%,#6f7a62 40%,#b8b8b3 60%,#d0cfcb 100%)"></div>
</section>

<!-- Gallery -->
<section class="gallery" role="img" aria-label="Chainwire fence by a building"></section>
<div class="abs" style="left:0;top:3120px;width:1200px;height:746px;background:rgba(0,0,0,.35)"></div>
<h2 class="section-title" style="top:3200px">Work Gallery</h2>
<div class="tile" role="img" aria-label="Crew installing a fence footing" style="left:160px;top:3270px;width:223px;height:210px;background:linear-gradient(180deg,#6a8a4a 0%,#4d5a44 60%,#3f4a3a 100%)"></div>
<div class="tile" role="img" aria-label="Aluminium balustrade on a bridge deck" style="left:396px;top:3270px;width:406px;height:210px;background:linear-gradient(180deg,#9db4cf 0%,#b8bcc0 50%,#8a8c8e 100%)"></div>
<div class="tile" role="img" aria-label="Black steel cage enclosure" style="left:817px;top:3270px;width:223px;height:210px;background:linear-gradient(180deg,#7d8593 0%,#3b3f48 55%,#55585c 100%)"></div>
<div class="tile" role="img" aria-label="Pool fence beside a new building" style="left:160px;top:3496px;width:223px;height:211px;background:linear-gradient(180deg,#4f86d1 0%,#b7c0c6 55%,#d9d7d2 100%)"></div>
<div class="tile" role="img" aria-label="Fenced sports court" style="left:396px;top:3496px;width:226px;height:211px;background:linear-gradient(180deg,#b8cbe0 0%,#7b8a6a 50%,#69705d 100%)"></div>
<div class="tile" role="img" aria-label="Steel handrail along a curved concrete path" style="left:633px;top:3496px;width:407px;height:211px;background:linear-gradient(180deg,#6b7d52 0%,#8e6e4e 50%,#c6c3bb 100%)"></div>
<a class="btn" style="left:533px;top:3734px;width:134px;height:41px">Explore More</a>

<!-- Safety -->
<div class="safety">Safety Is a Priority on All of Our Work Sites, We Ensure a Site<br>Specific SWMS And Risk Assesment Is Generated &amp; Followed<br>By All Staff Members.</div>
<a class="btn" style="left:533px;top:4088px;width:134px;height:41px">Contact Us</a>

<!-- Footer -->
<footer class="footer"></footer>
<div class="brand" style="left:0;width:1200px;justify-content:center;top:4282px;font-size:40px;line-height:48px"><i style="width:18px;height:18px"></i>Kolvenda Works</div>
<nav class="nav" style="left:383px;top:4373px;gap:42px;font-size:12px"><a>Home</a><a>Projects</a><a>About</a><a>Products</a><a>Contact Us</a></nav>
<div class="rule"></div>
<div class="contact" style="left:240px">
  <div class="ico"><svg width="16" height="18" viewBox="0 0 16 18"><path d="M8 1a6 6 0 0 0-6 6c0 4.5 6 10 6 10s6-5.5 6-10a6 6 0 0 0-6-6z" fill="none" stroke="#4fa61a" stroke-width="1.6"/><circle cx="8" cy="7" r="2" fill="#4fa61a"/></svg></div>
  <div>14 Larwick St<br>Marrindale NSW 2190</div>
</div>
<div class="contact" style="left:512px">
  <div class="ico"><svg width="16" height="16" viewBox="0 0 16 16"><path d="M3 1l3 1 1 3-2 1.5a9 9 0 0 0 4.5 4.5L11 9l3 1 1 3-2 2C7 15 1 9 1 3z" fill="#4fa61a"/></svg></div>
  <div>Phone No<br>02 9154 3270</div>
</div>
<div class="contact" style="left:755px">
  <div class="ico"><svg width="16" height="12" viewBox="0 0 16 12"><rect x="1" y="1" width="14" height="10" fill="none" stroke="#4fa61a" stroke-width="1.6"/><path d="M1 1l7 6 7-6" fill="none" stroke="#4fa61a" stroke-width="1.6"/></svg></div>
  <div>Email<br>info@kolvendaworks.com.au</div>
</div>
<div class="bar">
  <div class="l">© 2023 Kolvenda Pty Ltd. All Rights Reserved.</div>
  <div class="r">Privace &amp; Policy &nbsp;|&nbsp; Terms</div>
</div>

</body>
</html>
```